Yard sign design for high end luxury home builder.

Need a design for signage on custom homes that are being built. I already have a logo that I am satisfied with that needs to be incorporated. I need the following incorporated in the design of the sign-
- Lic number 318562
- phone number (555) 271-4038
- pendrickhomeworks.com
- Logo/Branding

If possible it may be nice to have the following quote that is on are business cards-

Quote from Osmund of Veltarra-
HE WHO WORKS WITH HIS HANDS IS A LABORER.
HE WHO WORKS WITH HIS HANDS & HIS HEAD IS A CRAFTSMAN.
HE WHO WORKS WITH HIS HANDS & HIS HEAD & HIS HEART IS AN ARTISAN.
-OSMUND OF VELTARRA

Target Market(s)

Archetect, Designers, Clients desiring to build a new home or remodel.

Colors
fde9d4
fee4d5
fabb94
fac994
faa54b
f68d4d
f37122
f78f20
f68e4e

Requirements
Must have
• - Lic number 318562
• - phone number (555) 271-4038
• - pendrickhomeworks.com
• - Logo/Branding
Nice to have
• Quote from Osmund of Veltarra-
• HE WHO WORKS WITH HIS HANDS IS A LABORER.
• HE WHO WORKS WITH HIS HANDS & HIS HEAD IS A CRAFTSMAN.
• HE WHO WORKS WITH HIS HANDS & HIS HEAD & HIS HEART IS AN ARTISAN.
• -OSMUND OF VELTARRA
• OR the below statement-
• Craftsmen that Care
Should not have
• Any additional verbiage not specified above including any type of verbiage about what kind of company we are. For instance- Integrity, reputable... It's just all played out. Im just looking for a bitching design that has the info that compliments my logo/branding.

```html
<!DOCTYPE html>
<html lang="en">
<head>
<meta charset="utf-8">
<title>Pendrick Homeworks Yard Sign</title>
<link rel="stylesheet" href="https://fonts.googleapis.com/css2?family=Arimo:wght@400;700&display=swap">
<style>
  :root {
    --ink: #0d0d0d;
    --tan: #a88b6a;
    --concrete-light: #eeeeee;
    --concrete-dark: #d6d6d6;
    --white: #ffffff;
  }
  html, body {
    margin: 0;
    padding: 0;
    width: 1200px;
    height: 767px;
    overflow: hidden;
    background: var(--white);
  }
  .yard-sign {
    display: block;
    width: 1200px;
    height: 767px;
    font-family: "Arimo", Arial, sans-serif;
  }
  .frame { fill: var(--ink); }
  .band { fill: var(--tan); }
  .quote-line { fill: var(--ink); font-weight: 700; }
  .brand-name { fill: var(--tan); font-weight: 700; }
  .brand-mark { fill: var(--tan); }
  .phone { fill: var(--ink); font-weight: 700; }
  .website { fill: var(--ink); font-weight: 400; }
  .license-label { fill: var(--white); font-weight: 700; }
  .license-number { fill: var(--tan); font-weight: 700; }
</style>
</head>
<body>
<svg class="yard-sign" viewBox="0 0 1439 920" xmlns="http://www.w3.org/2000/svg">
  <defs>
    <linearGradient id="concrete" x1="0" y1="0" x2="1" y2="1">
      <stop offset="0" stop-color="var(--concrete-light)"/>
      <stop offset="1" stop-color="var(--concrete-dark)"/>
    </linearGradient>
  </defs>

  <!-- background surface -->
  <rect width="1439" height="920" fill="url(#concrete)" role="img" aria-label="Light grey concrete texture background"/>

  <!-- outer frame -->
  <rect class="frame" x="0" y="0" width="1439" height="40"/>
  <rect class="frame" x="0" y="905" width="1439" height="15"/>

  <!-- brand panel -->
  <polygon class="frame" points="0,40 432,40 322,342 0,342"/>
  <rect class="brand-mark" x="46" y="62" width="120" height="120"/>
  <text class="brand-name" x="46" y="262" font-size="56" textLength="240" lengthAdjust="spacingAndGlyphs">PENDRICK</text>
  <text class="brand-name" x="46" y="308" font-size="27" textLength="240" lengthAdjust="spacingAndGlyphs">HOMEWORKS INC.</text>

  <!-- quote bands -->
  <polygon class="band" points="545,137 1439,137 1439,222 515,222"/>
  <polygon class="band" points="583,270 1439,270 1439,373 548,373"/>
  <polygon class="band" points="215,422 1439,422 1439,620 120,620"/>

  <text class="quote-line" x="585" y="212" font-size="90" textLength="795" lengthAdjust="spacingAndGlyphs">HE WHO WORKS</text>
  <text class="quote-line" x="610" y="355" font-size="90" textLength="770" lengthAdjust="spacingAndGlyphs">WITH HIS HANDS</text>
  <text class="quote-line" x="235" y="585" font-size="145" textLength="1140" lengthAdjust="spacingAndGlyphs">IS A LABORER</text>

  <!-- contact -->
  <text class="phone" x="48" y="760" font-size="100" textLength="802" lengthAdjust="spacingAndGlyphs">(555) 271-4038</text>
  <text class="website" x="65" y="865" font-size="56" textLength="775" lengthAdjust="spacingAndGlyphs">www.pendrickhomeworks.com</text>

  <!-- license panel -->
  <polygon class="frame" points="1040,685 1439,685 1439,905 950,905"/>
  <text class="license-label" x="1083" y="775" font-size="54" textLength="317" lengthAdjust="spacingAndGlyphs">Lic number</text>
  <text class="license-number" x="1088" y="860" font-size="86" textLength="302" lengthAdjust="spacingAndGlyphs">318562</text>
</svg>
</body>
</html>
```